Submission of a Belvostra Powerpoint Design

a PPT template for a new construction consulting and procurement advisory company, focused on collaborative contracting, operational excellence, project/contract/financial management. To be used for i) corporate presentations and ii) presenting consultancy proposals to clients. Audience: senior executives in the construction sector, developers and public authorities.
I want a modern and professional look that uses our brand colours and brand logo, sans serif font (humanist/modern/geometric), including an appropriate colour palette, white content slides containing a bar/area with logo & brand colours, transition slides containing header & large pictures, …I believe approx. 15 slides should be sufficient for a template, covering for instance :

A frontpage / introduction slide
“About us” slide
A closure / “thank you” slide
Contact information slide
Index / agenda slide
1 or 2 formats (with header/subheaders) for:
·

a transition slide (only visual/picture & a header)
Text-focused slide
Quote or testimonial slide
Image-focused slide
Chart/graph slide
Process flowchart slide
Case study slide (combination of text & images)
Summary slide (key takeaways, listing, etc.) as a listing
Summary slide as a matrix (e.g. 2x2, 2x3, 1x4 fields)
Please provide some appropriate icons.
Kindly look at www.belvostra-demo.com for some inspiration and feel

Target Market(s)

senior executives in the construction sector, developers, clients and public authorities

Industry/Entity Type

construction industry

Font styles to use
Sans Serif

Requirements
Must have
• A frontpage / introduction slide “About us” slide A closure / “thank you” slide Contact information slide Index / agenda slide 1 or 2 formats (with header/subheaders) for: · a transition slide (only visual/picture & a header) Text-focused slide Quote or testimonial slide Image-focused slide Chart/graph slide Process flowchart slide Case study slide (combination of text & images) Summary slide (key takeaways, listing, etc.) as a listing Summary slide as a matrix (e.g. 2x2, 2x3, 1x4 fields)
Nice to have
• For bullet points we would like to consider to use the circle without the BV.
Should not have
• Note the main logo is just the Belvostra word, the BV with circle is a separate image. Slides should not have excessive tacky decor (waves, etc)

```html
<!DOCTYPE html>
<html lang="en">
<head>
<meta charset="utf-8">
<title>Belvostra presentation template overview</title>
<link rel="stylesheet" href="https://fonts.googleapis.com/css2?family=Roboto+Condensed:wght@700&family=Roboto:wght@300;400;500;700&display=swap">
<style>
:root{
  --page:#eef4f6;
  --ink:#2f3b3e;
  --dark:#3e4749;
  --teal:#2b8587;
  --teal-deep:#246f72;
  --text:#7a8486;
  --card-line:#e6ecee;
  --band:linear-gradient(90deg,#3e4749 0%,#2f6c6f 60%,#2b8587 100%);
  --dark-bg:linear-gradient(120deg,#424a4c 0%,#365f62 50%,#2b8587 100%);
}
*{box-sizing:border-box;margin:0;padding:0}
html,body{width:1200px;height:1190px;overflow:hidden;background:var(--page)}
body{position:relative;font-family:'Roboto',sans-serif;color:var(--ink)}
.slide{position:absolute;width:352px;height:198px;background:#fff;overflow:hidden;box-shadow:0 1px 5px rgba(40,60,65,.14)}
.slide.dark{background:var(--dark-bg);color:#fff}
.abs{position:absolute}
.s-title{position:absolute;left:20px;top:6px;font:700 16px 'Roboto Condensed',sans-serif;color:var(--ink);letter-spacing:.2px}
.dark .s-title{color:#fff}
.s-sub{position:absolute;right:20px;top:8px;font:500 10.5px 'Roboto',sans-serif;color:var(--teal)}
.dark .s-sub{color:#fff}
.s-rule{position:absolute;left:0;top:27px;width:41px;height:1px;background:var(--teal)}
.s-rule::after{content:"";position:absolute;right:-1px;top:-1.5px;width:4px;height:4px;border-radius:50%;background:var(--teal)}
.dark .s-rule,.dark .s-rule::after{background:#fff}
.foot-bar{position:absolute;left:0;top:177px;width:264px;height:13px;background:var(--band)}
.foot-url{position:absolute;left:20px;top:3.5px;font:400 5.5px 'Roboto',sans-serif;color:#fff}
.foot-num{position:absolute;right:-1px;top:0;width:13px;height:13px;border-radius:50%;background:#fff;border:1.3px solid var(--teal);font:500 5.5px/10.5px 'Roboto',sans-serif;color:var(--ink);text-align:center}
.foot-logo{position:absolute;left:275px;top:177px;font:400 9.5px/13px 'Roboto',sans-serif;letter-spacing:1px;color:var(--teal-deep)}
.dark .foot-bar{background:rgba(255,255,255,.92)}
.dark .foot-url{color:var(--ink)}
.dark .foot-logo{color:#fff}
.wordmark{font:400 10px 'Roboto',sans-serif;letter-spacing:1.2px;color:#fff}
.photo{position:absolute;border-radius:1px}
.ic{width:100%;height:100%}
.icon-dot{position:absolute;border-radius:50%;background:var(--band);display:flex;align-items:center;justify-content:center}
.icon-dot svg{width:58%;height:58%}
.fine{font:400 3.6px/1.5 'Roboto',sans-serif;color:var(--text)}

/* cover */
.cover-welcome{left:20px;top:66px;font:700 6.5px 'Roboto',sans-serif}
.cover-name{left:20px;top:74px;font:700 16px 'Roboto Condensed',sans-serif;letter-spacing:.3px}
.cover-lede{left:20px;top:100px;width:130px;font:400 5.7px/1.85 'Roboto',sans-serif}
.cover-photo{left:178px;top:-8px;width:192px;height:192px;border-radius:50%;border:3px solid #fff;background:linear-gradient(150deg,#9aa3a6 0%,#c9c2b8 40%,#6f7b80 75%,#3b4548 100%)}

/* testimonials */
.quote-card{position:absolute;top:58px;width:93px;height:84px;background:#fff;border-radius:3px;box-shadow:0 1px 4px rgba(0,0,0,.12);text-align:center}
.quote-avatar{position:absolute;left:35px;top:6px;width:23px;height:23px;border-radius:50%;border:1.5px solid var(--card-line);background:linear-gradient(160deg,#c7b3a2,#5a4d47)}
.quote-text{position:absolute;left:6px;top:34px;width:81px;font:400 4.2px/1.95 'Roboto',sans-serif;color:var(--text)}
.quote-mark{position:absolute;font:700 17px/1 'Roboto',sans-serif;color:#dde2e4}
.quote-name{position:absolute;left:0;width:100%;top:72px;font:500 4.4px 'Roboto',sans-serif;color:var(--teal)}

/* listing cards */
.list-card{position:absolute;width:99px;height:57px;background:#fff;border-radius:2px;box-shadow:0 1px 4px rgba(0,0,0,.1)}
.list-card .icon-dot{left:5px;top:6px;width:15px;height:15px}
.list-card h4{position:absolute;left:24px;top:9px;width:72px;font:500 4.3px/1.35 'Roboto',sans-serif;color:var(--ink);text-transform:uppercase}
.list-card p{position:absolute;left:5px;top:27px;width:89px;text-align:justify}

/* agenda */
.agenda-back{left:-14px;top:98px;transform:rotate(-90deg);font:700 22px 'Roboto Condensed',sans-serif;color:rgba(255,255,255,.14);letter-spacing:1.5px}
.agenda-item{position:absolute;display:flex;align-items:center;gap:5px;font:500 6px 'Roboto',sans-serif;color:#fff}
.agenda-num{width:13px;height:13px;border-radius:50%;border:1px solid #fff;font:500 6px/11px 'Roboto',sans-serif;text-align:center}

/* sectors */
.sector{position:absolute;width:72px;height:53px;display:flex;align-items:center;justify-content:center;font:500 4.6px/1.3 'Roboto',sans-serif;color:#fff;text-align:center;border:1px solid #fff;box-shadow:0 0 2px rgba(0,0,0,.2)}

/* matrix */
.matrix{position:absolute;left:107px;top:58px;width:192px;height:81px;border-radius:3px;background:var(--band)}
.m-head{position:absolute;top:3px;width:62px;font:500 5px 'Roboto',sans-serif;color:#fff;text-align:center}
.m-cell{position:absolute;width:61px;height:25px;background:#fff;border-radius:2px;font:400 4.3px/1.5 'Roboto',sans-serif;color:var(--text);text-align:center;padding-top:6px}
.m-row{position:absolute;left:52px;font:500 5px 'Roboto',sans-serif;color:var(--teal)}

/* about */
.about-photo{left:20px;top:37px;width:143px;height:127px;border-radius:7px;background:linear-gradient(180deg,#8fb3d3 0%,#b49a80 45%,#6e5a4a 70%,#2e4f63 100%)}
.para{position:absolute;left:180px;width:152px;padding-left:9px;text-align:justify}
.para::before,.bullet::before{content:"";position:absolute;left:0;top:1px;width:3.5px;height:3.5px;border-radius:50%;border:.7px solid var(--text)}

/* chart panel */
.chart-panel{left:228px;top:39px;width:104px;height:126px;border-radius:3px;background:var(--dark-bg)}
.panel-item{position:absolute;left:6px;width:94px}
.panel-item .icon-dot{left:0;top:2px;width:12px;height:12px;background:#fff}
.panel-item h5{position:absolute;left:27px;top:0;font:500 3.8px 'Roboto',sans-serif;color:#fff}
.panel-item p{position:absolute;left:27px;top:6px;width:67px;font:400 2.9px/1.45 'Roboto',sans-serif;color:rgba(255,255,255,.85)}

/* why choose */
.why-frame{position:absolute;top:61px;width:81px;height:80px;border:.8px dashed #8fa0a3;border-radius:2px}
.why-frame.solid{border-style:solid}
.why-box{position:absolute;left:6px;top:6px;width:69px;height:68px;text-align:center;color:#fff;padding-top:10px}
.why-box svg{width:13px;height:13px}
.why-box h5{font:500 4.6px 'Roboto',sans-serif;margin-top:3px}
.why-box p{font:400 3.3px/1.5 'Roboto',sans-serif;color:rgba(255,255,255,.85);margin-top:2px;padding:0 4px}

/* flowchart */
.flow-title{position:absolute;left:182px;font:500 5px 'Roboto',sans-serif;color:var(--ink)}
.flow-text{position:absolute;left:182px;width:150px;font:400 4.1px/1.5 'Roboto',sans-serif;color:var(--text)}

/* contact */
.contact-card{position:absolute;width:99px;height:52px;border:.8px solid rgba(255,255,255,.55);background:rgba(255,255,255,.06);text-align:center;color:#fff}
.contact-pin{position:absolute;left:43px;top:-6px;width:12px;height:12px;border-radius:50%;background:#fff;display:flex;align-items:center;justify-content:center}
.contact-pin svg{width:7px;height:7px}
.contact-card h5{margin-top:11px;font:500 4.6px 'Roboto',sans-serif}
.contact-card h5::after{content:"";display:block;width:10px;height:.6px;background:#fff;margin:1.5px auto 0}
.contact-card p{font:400 3.6px/2.2 'Roboto',sans-serif;margin-top:2px}

/* benefits */
.bullet{position:relative;padding-left:9px;margin-bottom:6px;font:400 4.4px/1.65 'Roboto',sans-serif;color:var(--text);text-align:justify}
.bullet::before{top:1.5px}

/* case */
.case-label{position:absolute;font:500 4.8px/1.4 'Roboto',sans-serif;color:var(--ink)}
</style>
</head>
<body>

<svg width="0" height="0" style="position:absolute" aria-hidden="true">
  <defs>
    <symbol id="i-doc" viewBox="0 0 24 24"><g fill="none" stroke="currentColor" stroke-width="1.6"><rect x="5" y="3" width="14" height="18" rx="1.5"/><path d="M8 8h8M8 12h8M8 16h5"/></g></symbol>
    <symbol id="i-chart" viewBox="0 0 24 24"><g fill="none" stroke="currentColor" stroke-width="1.6"><path d="M4 20h16"/><rect x="6" y="12" width="3" height="8"/><rect x="11" y="8" width="3" height="12"/><rect x="16" y="4" width="3" height="16"/></g></symbol>
    <symbol id="i-team" viewBox="0 0 24 24"><g fill="none" stroke="currentColor" stroke-width="1.6"><circle cx="8" cy="8" r="3"/><circle cx="16" cy="8" r="3"/><path d="M3 19c0-3 2.5-5 5-5s5 2 5 5M11 19c0-3 2.5-5 5-5s5 2 5 5"/></g></symbol>
    <symbol id="i-gear" viewBox="0 0 24 24"><g fill="none" stroke="currentColor" stroke-width="1.6"><circle cx="12" cy="12" r="4"/><path d="M12 2v4M12 18v4M2 12h4M18 12h4M5 5l3 3M16 16l3 3M5 19l3-3M16 8l3-3"/></g></symbol>
    <symbol id="i-pin" viewBox="0 0 24 24"><path fill="currentColor" d="M12 2a7 7 0 0 0-7 7c0 5 7 13 7 13s7-8 7-13a7 7 0 0 0-7-7zm0 9.5A2.5 2.5 0 1 1 12 6.5a2.5 2.5 0 0 1 0 5z"/></symbol>
    <symbol id="i-rocket" viewBox="0 0 24 24"><g fill="none" stroke="currentColor" stroke-width="1.6"><path d="M14 4c3-1 6-1 6-1s0 3-1 6l-7 7-5-5z"/><path d="M7 11l-3 1 2 2M13 17l-1 3-2-2"/></g></symbol>
  </defs>
</svg>

<!-- 1 Cover -->
<section class="slide dark" style="left:41px;top:38px">
  <div class="abs wordmark" style="left:20px;top:13px">BELVOSTRA</div>
  <div class="abs cover-welcome">WELCOME TO</div>
  <div class="abs cover-name">BELVOSTRA</div>
  <p class="abs cover-lede">Belvostra is an infrastructure consultancy partnership specializing in the global construction industry.</p>
  <div class="abs cover-photo" role="img" aria-label="Photo of two consultants reviewing project documents"></div>
</section>

<!-- 6 Testimonials -->
<section class="slide" style="left:424px;top:38px">
  <h2 class="s-title">TESTIMONIALS</h2><div class="s-sub">What Our Customers Say</div><div class="s-rule"></div>
  <div class="quote-card" style="left:28px"><div class="quote-avatar" role="img" aria-label="Client portrait"></div><span class="quote-mark" style="left:5px;top:34px">“</span><p class="quote-text">Lorem ipsum dolor sit amet, consectet adipiscing elit, sed do eiusmodte incididunt ut labore et dolore magna aliqua ut enim ad minim.</p><span class="quote-mark" style="right:5px;top:56px">”</span><div class="quote-name">- ALEX MORROW</div></div>
  <div class="quote-card" style="left:129px"><div class="quote-avatar" role="img" aria-label="Client portrait"></div><span class="quote-mark" style="left:5px;top:34px">“</span><p class="quote-text">Lorem ipsum dolor sit amet, consectet adipiscing elit, sed do eiusmodte incididunt ut labore et dolore magna aliqua ut enim ad minim.</p><span class="quote-mark" style="right:5px;top:56px">”</span><div class="quote-name">- ALEX MORROW</div></div>
  <div class="quote-card" style="left:230px"><div class="quote-avatar" role="img" aria-label="Client portrait"></div><span class="quote-mark" style="left:5px;top:34px">“</span><p class="quote-text">Lorem ipsum dolor sit amet, consectet adipiscing elit, sed do eiusmodte incididunt ut labore et dolore magna aliqua ut enim ad minim.</p><span class="quote-mark" style="right:5px;top:56px">”</span><div class="quote-name">- ALEX MORROW</div></div>
  <div class="foot-bar"><span class="foot-url">https://www.belvostra-demo.com/</span><span class="foot-num">6</span></div><div class="foot-logo">BELVOSTRA</div>
</section>

<!-- 11 Summary listing -->
<section class="slide" style="left:808px;top:38px">
  <h2 class="s-title">SUMMARY SLIDE</h2><div class="s-sub">Our Solutions</div><div class="s-rule"></div>
  <div class="list-card" style="left:22px;top:42px"><span class="icon-dot" style="color:#fff"><svg><use href="#i-doc"/></svg></span><h4>Procurement and contract management</h4><p class="fine">We are able to manage a multiple stage procurement &amp; contract management process throughout a projects life cycle.</p></div>
  <div class="list-card" style="left:127px;top:42px"><span class="icon-dot" style="color:#fff"><svg><use href="#i-gear"/></svg></span><h4>Project management</h4><p class="fine">Together with our clients we build successful project management teams.</p></div>
  <div class="list-card" style="left:231px;top:42px"><span class="icon-dot" style="color:#fff"><svg><use href="#i-chart"/></svg></span><h4>Process management</h4><p class="fine">Process management helps you structure integrated projects in a structured way that makes project control more effective.</p></div>
  <div class="list-card" style="left:22px;top:104px"><span class="icon-dot" style="color:#fff"><svg><use href="#i-chart"/></svg></span><h4>Project finance management</h4><p class="fine">We specialise in strategic planning and infrastructure finance for critical infrastructure projects. We can manage all financial aspects of a project cycle.</p></div>
  <div class="list-card" style="left:127px;top:104px"><span class="icon-dot" style="color:#fff"><svg><use href="#i-team"/></svg></span><h4>Organizational coaching</h4><p class="fine">Systemic change within a firm is the focus of organizational coaching. It frequently overlaps with executive coaching.</p></div>
  <div class="list-card" style="left:231px;top:104px"><span class="icon-dot" style="color:#fff"><svg><use href="#i-doc"/></svg></span><h4>Procurement and contract management</h4><p class="fine">We are able to manage a multiple stage procurement &amp; contract management process throughout a projects life cycle.</p></div>
  <div class="foot-bar"><span class="foot-url">https://www.belvostra-demo.com/</span><span class="foot-num">11</span></div><div class="foot-logo">BELVOSTRA</div>
</section>

<!-- 2 Agenda -->
<section class="slide dark" style="left:41px;top:267px">
  <div class="abs wordmark" style="left:20px;top:14px">BELVOSTRA</div>
  <div class="abs agenda-back">AGENDA</div>
  <div class="agenda-item" style="left:100px;top:20px"><span class="agenda-num">1</span>INTRODUCTION</div>
  <div class="agenda-item" style="left:100px;top:44px"><span class="agenda-num">3</span>ABOUT US</div>
  <div class="agenda-item" style="left:100px;top:68px"><span class="agenda-num">4</span>TRANSITION</div>
  <div class="agenda-item" style="left:100px;top:92px"><span class="agenda-num">5</span>PROJECT BENEFITS</div>
  <div class="agenda-item" style="left:100px;top:116px"><span class="agenda-num">6</span>TESTIMONIALS</div>
  <div class="agenda-item" style="left:100px;top:140px"><span class="agenda-num">7</span>OUR SECTORS</div>
  <div class="agenda-item" style="left:100px;top:164px"><span class="agenda-num">8</span>CHART/GRAPH</div>
  <div class="agenda-item" style="left:210px;top:20px"><span class="agenda-num">9</span>PROCESS FLOWCHART</div>
  <div class="agenda-item" style="left:210px;top:44px"><span class="agenda-num">10</span>CASE STUDY</div>
  <div class="agenda-item" style="left:210px;top:68px"><span class="agenda-num">11</span>SOLUTION SUMMARY</div>
  <div class="agenda-item" style="left:210px;top:92px"><span class="agenda-num">12</span>MATRIX SUMMARY</div>
  <div class="agenda-item" style="left:210px;top:116px"><span class="agenda-num">13</span>WHY CHOOSE US</div>
  <div class="agenda-item" style="left:210px;top:140px"><span class="agenda-num">14</span>CONTACT US</div>
  <div class="agenda-item" style="left:210px;top:164px"><span class="agenda-num">15</span>THANK YOU</div>
</section>

<!-- 7 Sectors -->
<section class="slide" style="left:424px;top:267px">
  <h2 class="s-title">OUR SECTORS</h2><div class="s-sub">Image Focused</div><div class="s-rule"></div>
  <div class="sector" style="left:21px;top:45px;background:linear-gradient(180deg,#8aa6c4,#b8703f 55%,#2f4b6e)" role="img" aria-label="Container port at dusk">MARITIME</div>
  <div class="sector" style="left:100px;top:45px;background:linear-gradient(180deg,#9aa7ae,#5d6e77 60%,#3a4a55)" role="img" aria-label="Offshore platform at sea">OFFSHORE</div>
  <div class="sector" style="left:179px;top:45px;background:linear-gradient(180deg,#2b3c5a,#4a6c92 55%,#1d2838)" role="img" aria-label="Industrial plant at night">INDUSTRIAL</div>
  <div class="sector" style="left:258px;top:45px;background:linear-gradient(180deg,#3a5f84,#1f3552 60%,#0f1a2a)" role="img" aria-label="Telecom tower and city">TELECOM</div>
  <div class="sector" style="left:21px;top:106px;background:linear-gradient(180deg,#2c3e58,#4f6a8c 50%,#1b2638)" role="img" aria-label="Railway tunnel">RAIL / ROAD</div>
  <div class="sector" style="left:100px;top:106px;background:linear-gradient(180deg,#c6d2d8,#6f9a68 55%,#3a6a3c)" role="img" aria-label="Green urban district">URBAN<br>DEVELOPMENT</div>
  <div class="sector" style="left:179px;top:106px;background:linear-gradient(160deg,#6e8a5c,#2f6f84 50%,#1d4f6e)" role="img" aria-label="Aerial view of water reservoir">WATER</div>
  <div class="sector" style="left:258px;top:106px;background:linear-gradient(180deg,#5a6f8e,#e39a58 60%,#7a4a3a)" role="img" aria-label="Aircraft at sunset">AVIATION</div>
  <div class="foot-bar"><span class="foot-url">https://www.belvostra-demo.com/</span><span class="foot-num">7</span></div><div class="foot-logo">BELVOSTRA</div>
</section>

<!-- 12 Matrix -->
<section class="slide" style="left:808px;top:267px">
  <h2 class="s-title">SUMMARY SLIDE</h2><div class="s-sub">Our Matrix</div><div class="s-rule"></div>
  <div class="m-row" style="top:90px">LORUM IPSUM</div>
  <div class="m-row" style="top:120px">LORUM IPSUM</div>
  <div class="matrix">
    <div class="m-head" style="left:1px;top:9px">AT ACCUSEA</div>
    <div class="m-head" style="left:65px;top:9px">AT ACCUSEA</div>
    <div class="m-head" style="left:129px;top:9px">AT ACCUSEA</div>
    <div class="m-cell" style="left:2px;top:25px">Sed ut perspiciatis unde<br>omnis iste natus</div>
    <div class="m-cell" style="left:65px;top:25px">Sed ut perspiciatis unde<br>omnis iste natus</div>
    <div class="m-cell" style="left:129px;top:25px">Sed ut perspiciatis unde<br>omnis iste natus</div>
    <div class="m-cell" style="left:2px;top:53px">Sed ut perspiciatis unde<br>omnis iste natus</div>
    <div class="m-cell" style="left:65px;top:53px">Sed ut perspiciatis unde<br>omnis iste natus</div>
    <div class="m-cell" style="left:129px;top:53px">Sed ut perspiciatis unde<br>omnis iste natus</div>
  </div>
  <div class="foot-bar"><span class="foot-url">https://www.belvostra-demo.com/</span><span class="foot-num">12</span></div><div class="foot-logo">BELVOSTRA</div>
</section>

<!-- 3 About -->
<section class="slide" style="left:41px;top:496px">
  <h2 class="s-title">ABOUT US</h2><div class="s-sub">Who We Are</div><div class="s-rule"></div>
  <div class="photo about-photo" role="img" aria-label="Dam and arch bridge in a desert canyon"></div>
  <p class="para fine" style="top:46px">Belvostra is here to help as your trusted partner. By collaborating early with key parties and stakeholders, we identify and structure the best solution for your project.</p>
  <p class="para fine" style="top:71px">Once your project is underway, Belvostra is committed to its success with continued support. Our team provides advice for infrastructure projects to owners, developers, contractors, lenders, and investors.</p>
  <p class="para fine" style="top:101px">Belvostra specializes in strategic planning and financing for crucial infrastructure projects. Our focus is on large, complex, or high-risk projects. Working together with our clients, our integrated team gains a thorough understanding of requirements, which facilitates innovation and cost savings.</p>
  <p class="para fine" style="top:141px">With a global team of experienced partners, Belvostra brings decades of international experience to the table, ensuring the success of your infrastructure project.</p>
  <div class="foot-bar"><span class="foot-url">https://www.belvostra-demo.com/</span><span class="foot-num">3</span></div><div class="foot-logo">BELVOSTRA</div>
</section>

<!-- 8 Chart -->
<section class="slide" style="left:424px;top:496px">
  <h2 class="s-title">CHART/GRAPH</h2><div class="s-sub">Lorem ipsum dolor</div><div class="s-rule"></div>
  <svg class="abs" style="left:6px;top:36px" width="212" height="136" viewBox="0 0 212 136" font-family="Roboto, sans-serif">
    <g stroke="#e3e8ea" stroke-width=".5">
      <line x1="20" y1="8" x2="205" y2="8"/><line x1="20" y1="27" x2="205" y2="27"/><line x1="20" y1="46" x2="205" y2="46"/><line x1="20" y1="65" x2="205" y2="65"/><line x1="20" y1="84" x2="205" y2="84"/><line x1="20" y1="103" x2="205" y2="103"/>
      <line x1="43" y1="8" x2="43" y2="122"/><line x1="69.5" y1="8" x2="69.5" y2="122"/><line x1="96" y1="8" x2="96" y2="122"/><line x1="122.5" y1="8" x2="122.5" y2="122"/><line x1="149" y1="8" x2="149" y2="122"/><line x1="175.5" y1="8" x2="175.5" y2="122"/><line x1="205" y1="8" x2="205" y2="122"/>
    </g>
    <line x1="20" y1="122" x2="205" y2="122" stroke="#b9c2c4" stroke-width=".6"/>
    <g font-size="4.6" fill="#3e4749" text-anchor="end">
      <text x="15" y="10">120</text><text x="15" y="29">100</text><text x="15" y="48">80</text><text x="15" y="67">60</text><text x="15" y="86">40</text><text x="15" y="105">20</text><text x="15" y="124">0</text>
    </g>
    <g fill="#3e4749">
      <rect x="25" y="27" width="3.5" height="95"/><rect x="51.5" y="36.5" width="3.5" height="85.5"/><rect x="78" y="74.5" width="3.5" height="47.5"/><rect x="104.5" y="27" width="3.5" height="95"/><rect x="131" y="27" width="3.5" height="95"/><rect x="157.5" y="65" width="3.5" height="57"/><rect x="184" y="74.5" width="3.5" height="47.5"/>
    </g>
    <g fill="#2b8587">
      <rect x="30.5" y="36.5" width="3.5" height="85.5"/><rect x="57" y="46" width="3.5" height="76"/><rect x="83.5" y="27" width="3.5" height="95"/><rect x="110" y="65" width="3.5" height="57"/><rect x="136.5" y="36.5" width="3.5" height="85.5"/><rect x="163" y="50.75" width="3.5" height="71.25"/><rect x="189.5" y="27" width="3.5" height="95"/>
    </g>
    <g font-size="4.2" fill="#3e4749" text-anchor="middle">
      <text x="26.8" y="24">100</text><text x="32.3" y="33.5">90</text><text x="53.3" y="33.5">90</text><text x="58.8" y="43">80</text><text x="79.8" y="71.5">50</text><text x="85.3" y="24">100</text><text x="106.3" y="24">100</text><text x="111.8" y="62">60</text><text x="132.8" y="24">100</text><text x="138.3" y="33.5">90</text><text x="159.3" y="62">60</text><text x="164.8" y="47.8">75</text><text x="185.8" y="71.5">50</text><text x="191.3" y="24">100</text>
    </g>
    <g font-size="4.6" fill="#3e4749" text-anchor="middle">
      <text x="30" y="131">Sun</text><text x="56.5" y="131">Mon</text><text x="83" y="131">Tue</text><text x="109.5" y="131">Wed</text><text x="136" y="131">Thu</text><text x="162.5" y="131">Fri</text><text x="189" y="131">Sat</text>
    </g>
  </svg>
  <div class="abs chart-panel">
    <div class="panel-item" style="top:15px"><span class="icon-dot" style="color:#2b8587"><svg><use href="#i-gear"/></svg></span><h5>PROCESS MANAGEMENT</h5><p>Process management helps you structure integrated projects in a structured way that makes project control more effective.</p></div>
    <div class="panel-item" style="top:49px"><span class="icon-dot" style="color:#2b8587"><svg><use href="#i-chart"/></svg></span><h5>PROJECT FINANCE MANAGEMENT</h5><p>We specialise in strategic planning and infrastructure finance for critical infrastructure projects. We can manage all financial aspects of a project cycle.</p></div>
    <div class="panel-item" style="top:83px"><span class="icon-dot" style="color:#2b8587"><svg><use href="#i-team"/></svg></span><h5>ORGANIZATIONAL COACHING</h5><p>Systemic change within a firm is the focus of organizational coaching. It frequently overlaps with executive coaching, when the individual's development is the main objective.</p></div>
  </div>
  <div class="foot-bar"><span class="foot-url">https://www.belvostra-demo.com/</span><span class="foot-num">8</span></div><div class="foot-logo">BELVOSTRA</div>
</section>

<!-- 13 Why choose us -->
<section class="slide" style="left:808px;top:496px">
  <h2 class="s-title">WHY CHOOSE US</h2><div class="s-sub">Appropriate Icons</div><div class="s-rule"></div>
  <div class="why-frame" style="left:38px"><div class="why-box" style="background:#3e4749"><svg style="color:#fff"><use href="#i-doc"/></svg><h5>LOREM IPSUM</h5><p>Lorem ipsum dolor sit amet conse ctetur adipiscing elit sed do eiusmod tempor.</p></div></div>
  <div class="why-frame solid" style="left:135px"><div class="why-box" style="background:linear-gradient(160deg,#3e4749,#2b8587)"><svg style="color:#fff"><use href="#i-team"/></svg><h5>LOREM IPSUM</h5><p>Lorem ipsum dolor sit amet conse ctetur adipiscing elit sed do eiusmod tempor.</p></div></div>
  <div class="why-frame" style="left:232px;border-color:#2b8587"><div class="why-box" style="background:#2b8587"><svg style="color:#fff"><use href="#i-chart"/></svg><h5>LOREM IPSUM</h5><p>Lorem ipsum dolor sit amet conse ctetur adipiscing elit sed do eiusmod tempor.</p></div></div>
  <svg class="abs" style="left:119px;top:97px" width="16" height="8" viewBox="0 0 16 8"><path d="M0 4h14M11 1.5l3 2.5-3 2.5" fill="none" stroke="#3e4749" stroke-width=".8"/></svg>
  <svg class="abs" style="left:216px;top:97px" width="16" height="8" viewBox="0 0 16 8"><path d="M0 4h14M11 1.5l3 2.5-3 2.5" fill="none" stroke="#2b8587" stroke-width=".8"/></svg>
  <div class="foot-bar"><span class="foot-url">https://www.belvostra-demo.com/</span><span class="foot-num">13</span></div><div class="foot-logo">BELVOSTRA</div>
</section>

<!-- 4 Transition -->
<section class="slide" style="left:41px;top:725px">
  <h2 class="s-title">TRANSITION</h2><div class="s-sub">Lorem ipsum dolor</div><div class="s-rule"></div>
  <div class="photo" style="left:21px;top:41px;width:71px;height:56px;background:linear-gradient(180deg,#c9b99a,#7c8a95 55%,#3f5466)" role="img" aria-label="Ship moored at a harbour crane"></div>
  <div class="photo" style="left:100px;top:41px;width:71px;height:56px;background:linear-gradient(180deg,#b7c6d9,#7f94b3 60%,#5d7394)" role="img" aria-label="Offshore wind turbines in haze"></div>
  <div class="photo" style="left:180px;top:41px;width:71px;height:56px;background:linear-gradient(180deg,#3a4a56,#8e9ba3 55%,#2c3640)" role="img" aria-label="Server room corridor"></div>
  <div class="photo" style="left:258px;top:41px;width:72px;height:119px;background:linear-gradient(180deg,#e0a460,#6c8f6a 25%,#d9e0e3 55%,#a9b2b5 80%,#7d8a8e)" role="img" aria-label="Dam spillway releasing water"></div>
  <div class="photo" style="left:21px;top:104px;width:150px;height:56px;background:linear-gradient(170deg,#9ec9d2,#3ba5b4 50%,#1f6f8a)" role="img" aria-label="Aerial view of artificial palm island"></div>
  <div class="photo" style="left:180px;top:104px;width:71px;height:56px;background:radial-gradient(circle at 50% 45%,#3fa3d8,#1b3d66 55%,#2a2420)" role="img" aria-label="Lit road tunnel"></div>
  <div class="foot-bar"><span class="foot-url">https://www.belvostra-demo.com/</span><span class="foot-num">4</span></div><div class="foot-logo">BELVOSTRA</div>
</section>

<!-- 9 Process flowchart -->
<section class="slide" style="left:424px;top:725px">
  <h2 class="s-title">PROCESS FLOWCHART</h2><div class="s-sub">Lorem ipsum dolor</div><div class="s-rule"></div>
  <svg class="abs" style="left:0;top:0" width="352" height="177" viewBox="0 0 352 177">
    <defs><linearGradient id="flowGrad" x1="0" y1="0" x2="1" y2="1"><stop offset="0" stop-color="#3e4749"/><stop offset="1" stop-color="#2b8587"/></linearGradient></defs>
    <circle cx="75" cy="101" r="48" fill="none" stroke="#2b8587" stroke-width=".8"/>
    <circle cx="75" cy="101" r="42" fill="url(#flowGrad)"/>
    <g fill="none" stroke="#3e4749" stroke-width=".5">
      <path d="M107 66 L118 52 H148"/><path d="M120 87 H148"/><path d="M120 117 H148"/><path d="M107 135 L118 151 H148"/>
    </g>
    <g fill="#fff" stroke="#3e4749" stroke-width=".6"><circle cx="107" cy="66" r="1.3"/><circle cx="120" cy="87" r="1.3"/><circle cx="120" cy="117" r="1.3"/><circle cx="107" cy="135" r="1.3"/></g>
    <g fill="#fff" stroke="#2b8587" stroke-width="1.4"><circle cx="160" cy="52" r="11"/><circle cx="160" cy="84" r="11"/><circle cx="160" cy="119" r="11"/><circle cx="160" cy="151" r="11"/></g>
    <g fill="#3e4749"><circle cx="160" cy="52" r="8.3"/><circle cx="160" cy="84" r="8.3"/><circle cx="160" cy="119" r="8.3"/><circle cx="160" cy="151" r="8.3"/></g>
    <g color="#fff"><use href="#i-gear" x="155" y="47" width="10" height="10"/><use href="#i-rocket" x="155" y="79" width="10" height="10"/><use href="#i-doc" x="155" y="114" width="10" height="10"/><use href="#i-gear" x="155" y="146" width="10" height="10"/></g>
    <text x="75" y="104" text-anchor="middle" font-family="Roboto, sans-serif" font-size="10" letter-spacing="1" fill="#fff">BELVOSTRA</text>
  </svg>
  <div class="flow-title" style="top:39px">LOREM IPSUM DOLOR</div><div class="flow-text" style="top:47px">Sed ut perspiciatis unde omnis iste natus error sit voluptatem cusantium doloremque laudantium.</div>
  <div class="flow-title" style="top:71px">LOREM IPSUM DOLOR</div><div class="flow-text" style="top:79px">Sed ut perspiciatis unde omnis iste natus error sit voluptatem cusantium doloremque laudantium.</div>
  <div class="flow-title" style="top:106px">LOREM IPSUM DOLOR</div><div class="flow-text" style="top:114px">Sed ut perspiciatis unde omnis iste natus error sit voluptatem cusantium doloremque laudantium.</div>
  <div class="flow-title" style="top:138px">LOREM IPSUM DOLOR</div><div class="flow-text" style="top:146px">Sed ut perspiciatis unde omnis iste natus error sit voluptatem cusantium doloremque laudantium.</div>
  <div class="foot-bar"><span class="foot-url">https://www.belvostra-demo.com/</span><span class="foot-num">9</span></div><div class="foot-logo">BELVOSTRA</div>
</section>

<!-- 14 Contact -->
<section class="slide dark" style="left:808px;top:725px">
  <h2 class="s-title">CONTACT US</h2><div class="s-sub">Contact Information</div><div class="s-rule"></div>
  <div class="contact-card" style="left:22px;top:46px"><span class="contact-pin" style="color:#2b8587"><svg><use href="#i-pin"/></svg></span><h5>MAARTEN DELCOUR</h5><p>Lindenlaan 12 9100 Northvale, Belgium<br>☏ +32 400 11 22 33<br>✉ m.delcour@mailsample.com</p></div>
  <div class="contact-card" style="left:126px;top:46px"><span class="contact-pin" style="color:#2b8587"><svg><use href="#i-pin"/></svg></span><h5>OWEN HALLOWAY</h5><p>Based in Brightwater Queensland, Australia<br>☏ +61 (0)400 555 010<br>✉ halloway.advice@mailsample.com</p></div>
  <div class="contact-card" style="left:231px;top:46px"><span class="contact-pin" style="color:#2b8587"><svg><use href="#i-pin"/></svg></span><h5>TOBIAS VERHELST</h5><p>Harbor City – Panama<br>☏ +32 400 44 55 66<br>✉ tobias@sampleledger.com</p></div>
  <div class="contact-card" style="left:74px;top:111px"><span class="contact-pin" style="color:#2b8587"><svg><use href="#i-pin"/></svg></span><h5>PIETER VANMOL</h5><p>Based in Northport Belgium<br>☏ +32 400 77 88 99</p></div>
  <div class="contact-card" style="left:179px;top:111px"><span class="contact-pin" style="color:#2b8587"><svg><use href="#i-pin"/></svg></span><h5>RUBEN CASTAERT</h5><p>Based in Mexico<br>☏ +57 300 555 0142</p></div>
  <div class="foot-bar"><span class="foot-url">https://www.belvostra-demo.com/</span><span class="foot-num">14</span></div><div class="foot-logo">BELVOSTRA</div>
</section>

<!-- 5 Project benefits -->
<section class="slide" style="left:41px;top:954px">
  <h2 class="s-title">PROJECT BENEFITS</h2><div class="s-sub">Text Focused</div><div class="s-rule"></div>
  <div class="abs" style="left:20px;top:45px;width:152px">
    <p class="bullet">Clients should consider a collaborative approach in procuring a potential project in circumstances where:</p>
    <p class="bullet">The project risks are difficult to quantify fully, and innovative approaches are needed to manage this;</p>
    <p class="bullet">There is a need to obtain cost certainty while demonstrating transparency;</p>
    <p class="bullet">Project delivery timeframes are constrained;</p>
    <p class="bullet">You are interested in moving away from a transactional model towards a collaborative model, where the project is of insufficient size or complexity to fully resource a relationship based model such as an alliance;</p>
  </div>
  <div class="abs" style="left:180px;top:45px;width:152px">
    <p class="bullet">There is identified value in participating in a collaborative arrangement to drive innovative outcomes and knowledge transfer; and</p>
    <p class="bullet">There are uncertain or complex design or construction interfaces, and flexibility in scheduling and delivery within the entire supply chain is required.</p>
  </div>
  <div class="foot-bar"><span class="foot-url">https://www.belvostra-demo.com/</span><span class="foot-num">5</span></div><div class="foot-logo">BELVOSTRA</div>
</section>

<!-- 10 Case study -->
<section class="slide" style="left:424px;top:954px">
  <h2 class="s-title">CASE STUDY</h2><div class="s-sub">Lorem ipsum dolor</div><div class="s-rule"></div>
  <svg class="abs" style="left:0;top:0" width="352" height="177" viewBox="0 0 352 177">
    <circle cx="176" cy="121" r="38" fill="none" stroke="#2b8587" stroke-width=".8"/>
    <circle cx="176" cy="121" r="33" fill="#fff" stroke="#e3e8ea" stroke-width="2.5"/>
    <g fill="none" stroke="#3e4749" stroke-width=".5">
      <path d="M176 71 V83"/><path d="M118 92 L140 107"/><path d="M233 92 L212 107"/><path d="M118 150 L140 136"/><path d="M233 150 L212 136"/>
    </g>
    <g fill="#fff" stroke="#3e4749" stroke-width=".6"><circle cx="176" cy="83" r="1.3"/><circle cx="140" cy="107" r="1.3"/><circle cx="212" cy="107" r="1.3"/><circle cx="140" cy="136" r="1.3"/><circle cx="212" cy="136" r="1.3"/></g>
    <g fill="#fff" stroke="#2b8587" stroke-width="1.3"><circle cx="176" cy="61" r="10"/><circle cx="108" cy="92" r="10"/><circle cx="243" cy="92" r="10"/><circle cx="108" cy="150" r="10"/><circle cx="243" cy="150" r="10"/></g>
    <g fill="#3e4749"><circle cx="176" cy="61" r="7.5"/><circle cx="108" cy="92" r="7.5"/><circle cx="243" cy="92" r="7.5"/><circle cx="108" cy="150" r="7.5"/><circle cx="243" cy="150" r="7.5"/></g>
    <g color="#fff"><use href="#i-team" x="171.5" y="56.5" width="9" height="9"/><use href="#i-gear" x="103.5" y="87.5" width="9" height="9"/><use href="#i-chart" x="238.5" y="87.5" width="9" height="9"/><use href="#i-doc" x="103.5" y="145.5" width="9" height="9"/><use href="#i-team" x="238.5" y="145.5" width="9" height="9"/></g>
    <text x="176" y="124" text-anchor="middle" font-family="Roboto, sans-serif" font-size="7" letter-spacing=".8" fill="#2f3b3e">BELVOSTRA</text>
  </svg>
  <div class="case-label" style="left:0;width:352px;top:37px;text-align:center">INITIAL-ADVISORY SERVICES</div>
  <div class="case-label" style="left:30px;width:60px;top:84px;text-align:right">PROJECT / PROCESS MANAGEMENT</div>
  <div class="case-label" style="left:261px;width:70px;top:84px">PROJECT FINANCE MANAGEMENT</div>
  <div class="case-label" style="left:10px;width:80px;top:147px;text-align:right">CONTRACT MANAGEMENT</div>
  <div class="case-label" style="left:261px;width:90px;top:147px">ORGANIZATIONAL COACHING</div>
  <div class="foot-bar"><span class="foot-url">https://www.belvostra-demo.com/</span><span class="foot-num">10</span></div><div class="foot-logo">BELVOSTRA</div>
</section>

<!-- 15 Thank you -->
<section class="slide dark" style="left:808px;top:954px">
  <div class="abs" style="left:0;width:352px;top:60px;text-align:center;font:400 32px 'Roboto',sans-serif;letter-spacing:3px;color:#fff">BELVOSTRA</div>
  <div class="abs" style="left:0;width:352px;top:128px;text-align:center;font:700 18px 'Roboto Condensed',sans-serif;color:#fff">THANK YOU</div>
  <div class="abs" style="left:163px;top:152px;width:26px;height:1.2px;background:#fff"></div>
</section>

</body>
</html>
```